Top of the line business card design needed for real estate brokerage

We currently have a business card with our logo but would like to have a revised version. We would love for you to implement your own design that will catch anyone's attention. The theme colors should be black, royal blue, gray/silver, and white.The contact information should be the same as the info on our current business card (picture attached). In the design that we pick, we will need to be able to edit the text so that we can customize the text content for each of our agents. Same goes for the professional picture. There should be an area on the card that each agent can have their professional portrait attached. Please include a version without the picture option as well for agents that do not wish to have a professional picture attached.

```html
<!DOCTYPE html>
<html lang="en">
<head>
<meta charset="utf-8">
<title>Clear Harbor Realty – Business Card</title>
<link href="https://fonts.googleapis.com/css2?family=Source+Sans+3:ital,wght@0,400;0,600;0,700;1,400&family=PT+Serif:wght@400&display=swap" rel="stylesheet">
<style>
  :root {
    --royal: #0a4ea3;
    --ink: #222326;
    --text: #3a3d42;
    --silver: #a2a5aa;
    --icon: #b8bbbf;
    --paper: #ffffff;
    --backdrop: #ececec;
  }
  * { box-sizing: border-box; margin: 0; padding: 0; }
  html, body { width: 1200px; height: 1200px; overflow: hidden; }
  body {
    background: var(--backdrop);
    font-family: "Source Sans 3", "Segoe UI", sans-serif;
    color: var(--text);
    position: relative;
  }
  .card {
    position: absolute;
    width: 803px;
    height: 520px;
    background: var(--paper);
  }
  .card--front { left: 199px; top: 64px; }
  .card--back  { left: 198px; top: 616px; }

  /* Front */
  .portrait {
    position: absolute;
    left: 80px; top: 58px;
    width: 155px; height: 194px;
    background: linear-gradient(160deg, #1b1b1d 0%, #26201f 55%, #8e1b22 100%);
  }
  .brand {
    position: absolute;
    display: flex;
    align-items: center;
    gap: 12px;
    font-weight: 700;
    color: var(--ink);
    white-space: nowrap;
  }
  .brand__mark {
    width: 18px; height: 18px;
    background: var(--royal);
    flex: none;
  }
  .card--front .brand {
    left: 490px; top: 205px;
    font-size: 31px;
  }
  .agent { position: absolute; left: 76px; top: 298px; }
  .agent__name {
    font-size: 29px;
    font-weight: 700;
    color: var(--ink);
    line-height: 1;
  }
  .agent__role {
    margin-top: 8px;
    font-family: "PT Serif", Georgia, serif;
    font-size: 16px;
    color: var(--royal);
  }
  .contact {
    position: absolute;
    left: 482px; top: 312px;
    list-style: none;
    font-size: 16px;
    color: var(--text);
  }
  .contact__item {
    display: flex;
    align-items: flex-start;
    gap: 12px;
    line-height: 20px;
  }
  .contact__item + .contact__item { margin-top: 6px; }
  .contact__item--gap { margin-top: 16px !important; }
  .contact__icon { width: 17px; height: 17px; flex: none; margin-top: 2px; }
  .contact__item--address .contact__icon { margin-top: 11px; }
  .contact strong { font-weight: 600; }
  .contact em { font-style: italic; }
  .services-band {
    position: absolute;
    left: 0; right: 0; bottom: 0;
    height: 35px;
    background: var(--royal);
    color: #fff;
    font-size: 16px;
    display: flex;
    align-items: center;
    justify-content: center;
  }

  /* Back */
  .skyline {
    position: absolute;
    left: 34px; top: 32px;
    width: 735px; height: 390px;
    background: linear-gradient(180deg, rgba(226,227,229,0) 0%, rgba(226,227,229,0.55) 45%, rgba(226,227,229,0.7) 80%, rgba(226,227,229,0) 100%);
  }
  .card--back .brand {
    left: 0; right: 0; top: 230px;
    justify-content: center;
    font-size: 50px;
    gap: 16px;
  }
  .card--back .brand__mark { width: 26px; height: 26px; }
  .services-line {
    position: absolute;
    left: 0; right: 0; top: 480px;
    text-align: center;
    font-size: 16px;
    font-weight: 600;
    word-spacing: 1px;
  }
  .services-line span + span { margin-left: 6px; }
  .services-line .tone-blue { color: var(--royal); }
  .services-line .tone-ink { color: var(--ink); }
  .services-line .tone-silver { color: var(--silver); }
</style>
</head>
<body>

<section class="card card--front">
  <div class="portrait" role="img" aria-label="Agent professional portrait"></div>

  <div class="brand"><span class="brand__mark"></span>Clear Harbor Realty</div>

  <div class="agent">
    <h1 class="agent__name">Marisol Vantreck</h1>
    <p class="agent__role">Broker</p>
  </div>

  <ul class="contact">
    <li class="contact__item">
      <svg class="contact__icon" viewBox="0 0 24 24"><path fill="var(--icon)" d="M6.6 10.8a15.2 15.2 0 0 0 6.6 6.6l2.2-2.2c.3-.3.7-.4 1-.2 1.1.4 2.3.6 3.6.6.6 0 1 .4 1 1V20c0 .6-.4 1-1 1A17 17 0 0 1 3 4c0-.6.4-1 1-1h3.5c.6 0 1 .4 1 1 0 1.3.2 2.5.6 3.6.1.3 0 .7-.2 1z"/></svg>
      <span>555 <strong>210 3381</strong> | 555 <strong>210 3390</strong></span>
    </li>
    <li class="contact__item">
      <svg class="contact__icon" viewBox="0 0 24 24"><path fill="var(--icon)" d="M7 3h10v5H7zM4 9h16a2 2 0 0 1 2 2v6h-4v4H6v-4H2v-6a2 2 0 0 1 2-2zm4 6v4h8v-4z"/></svg>
      <span>555 <strong>210 4476</strong></span>
    </li>
    <li class="contact__item contact__item--gap">
      <svg class="contact__icon" viewBox="0 0 24 24"><path fill="var(--icon)" d="M2 6h20v12H2zm2 1.5 8 6 8-6z"/></svg>
      <em>marisol@clearharborrealty.com</em>
    </li>
    <li class="contact__item contact__item--gap contact__item--address">
      <svg class="contact__icon" viewBox="0 0 24 24"><path fill="var(--icon)" d="M12 2a7 7 0 0 0-7 7c0 5 7 13 7 13s7-8 7-13a7 7 0 0 0-7-7zm0 9.5A2.5 2.5 0 1 1 12 6.5a2.5 2.5 0 0 1 0 5z"/></svg>
      <span>820 Lantern Way, Suite 310<br>Harlow Point, FL 30412</span>
    </li>
  </ul>

  <div class="services-band">Residential Real Estate . Commercial Real Estate . Property Management . Investments</div>
</section>

<section class="card card--back">
  <div class="skyline" role="img" aria-label="Faint line drawing of a city skyline"></div>
  <div class="brand"><span class="brand__mark"></span>Clear Harbor Realty</div>
  <p class="services-line">
    <span class="tone-blue">Residential Real Estate</span><span class="tone-ink">Commercial Real Estate</span><span class="tone-blue">Property Management</span><span class="tone-silver">Investments</span>
  </p>
</section>

</body>
</html>
```